Design Shopify E-Commerce Website for Men's Products

Design a Shopify website for men to sell our men's jewelry, cigar and bar accessories, and other men's products. Design should be hip, with like a rock n' roll, biker, whiskey driker flare. Name of the company is "Ironvale Locker" and website will be www.IronvaleLocker.com
Homepage will have navigation bar with three categories: Men's Jewelry, Cigar & Bar Products, Man Cave Swag
I will upload our logo, inspiration type pictures and some of the products that we sell
Theme colors should be mainly dark: black, grey, brown, gold

```html
<!DOCTYPE html>
<html lang="en">
<head>
<meta charset="utf-8">
<title>Ironvale Locker</title>
<link rel="stylesheet" href="https://fonts.googleapis.com/css2?family=UnifrakturCook:wght@700&family=Poppins:wght@400;500;600&display=swap">
<style>
:root{
  --bg:#060606;
  --panel:#1d1d1d;
  --gold:#c9a23f;
  --gold-light:#ead9a4;
  --gold-dark:#a67c25;
  --text:#f2f2f2;
  --muted:#cfcfcf;
}
*{box-sizing:border-box;margin:0;padding:0}
html,body{width:1200px;height:4521px;overflow:hidden;background:var(--bg)}
body{position:relative;font-family:"Poppins",sans-serif;color:var(--text)}
.abs{position:absolute}
.display{font-family:"UnifrakturCook",serif;color:var(--gold);font-weight:700;line-height:1.05}
.lede{font-size:15px;line-height:1.55;color:var(--text)}
.btn{position:absolute;width:144px;height:39px;background:linear-gradient(90deg,var(--gold-light),var(--gold));color:#111;font-size:13px;font-weight:600;display:flex;align-items:center;justify-content:center;clip-path:polygon(0 0,100% 0,100% 70%,92% 100%,0 100%);letter-spacing:.3px}
.photo{position:absolute}
/* header */
.brand-mark{left:130px;top:58px;font-size:20px;font-weight:600;color:var(--gold);display:flex;align-items:center;gap:8px}
.brand-mark .dot{width:14px;height:14px;border-radius:50%;background:var(--gold)}
.main-nav{top:40px;font-size:14px;color:var(--text)}
.main-nav a{position:absolute;white-space:nowrap;color:inherit;text-decoration:none}
/* products */
.product{position:absolute;width:220px;text-align:center}
.product .thumb{width:190px;height:150px;margin:0 auto;border-radius:6px}
.product .name{margin-top:24px;font-size:16px}
.product .price{margin-top:8px;font-size:16px;font-weight:600;color:var(--gold)}
.footer-link{font-size:14px;color:var(--muted);position:absolute;left:128px}
.card-badge{width:36px;height:22px;border-radius:3px;display:inline-block;margin:0 4px;background:#e6e6e6}
</style>
</head>
<body>

<header class="site-header">
  <div class="abs brand-mark"><span class="dot"></span>Ironvale Locker</div>
  <nav class="abs main-nav" style="left:0;width:1200px">
    <a style="left:361px">Men's Jewelry</a>
    <a style="left:510px">Cigar &amp; Bar Products</a>
    <a style="left:712px">Man Cave Swag</a>
  </nav>
  <svg class="abs" style="left:982px;top:48px" width="90" height="20" viewBox="0 0 90 20" fill="var(--gold)">
    <circle cx="8" cy="8" r="5" fill="none" stroke="var(--gold)" stroke-width="2"/><line x1="11.5" y1="11.5" x2="16" y2="16" stroke="var(--gold)" stroke-width="2.4"/>
    <rect x="34" y="5" width="14" height="12" rx="2"/><path d="M37 6 V4 a4 4 0 0 1 8 0 V6" fill="none" stroke="var(--gold)" stroke-width="1.6"/>
    <circle cx="72" cy="6" r="4"/><path d="M65 17 a7 6 0 0 1 14 0z"/>
  </svg>
</header>

<section class="hero">
  <h1 class="abs display" style="left:126px;top:288px;font-size:54px">Ironvale<br>Locker</h1>
  <p class="abs lede" style="left:126px;top:419px;width:345px">Lorem ipsum dolor sit amet, consectetur adipiscing elit, sed do eiusmod tempor inc didunt ut labore et dolore magna.</p>
  <a class="btn" style="left:126px;top:510px">SHOP NOW</a>
  <div class="abs" style="left:874px;top:298px;width:238px;height:407px;border-right:7px solid var(--gold);border-bottom:7px solid var(--gold)"></div>
  <div class="photo" role="img" aria-label="Brandy glass with cigar and decanter in smoke on a wooden table" style="left:600px;top:153px;width:505px;height:542px;background:radial-gradient(circle at 45% 60%,#b8651e 0%,#6b3511 35%,#2b170a 70%,#120a05 100%)"></div>
</section>

<section class="products">
  <h2 class="abs display" style="left:0;width:1200px;text-align:center;top:847px;font-size:52px">Our Products</h2>
  <svg class="abs" style="left:70px;top:1026px" width="14" height="18" viewBox="0 0 14 18"><path d="M10 3 L4 9 L10 15" fill="none" stroke="var(--gold)" stroke-width="2.4"/></svg>
  <svg class="abs" style="left:1109px;top:1026px" width="14" height="18" viewBox="0 0 14 18"><path d="M4 3 L10 9 L4 15" fill="none" stroke="var(--gold)" stroke-width="2.4"/></svg>
  <div class="product" style="left:115px;top:956px"><div class="thumb" role="img" aria-label="Red lacquered cigar humidor" style="background:linear-gradient(160deg,#9c1f22,#5a0d10)"></div><div class="name">CIGAR HUMIDOR</div><div class="price">$29.00 USD</div></div>
  <div class="product" style="left:364px;top:956px"><div class="thumb" role="img" aria-label="Wooden whiskey set box with glasses" style="background:linear-gradient(160deg,#6a3a24,#2a1810)"></div><div class="name">WHISKEYSET</div><div class="price">$29.00 USD</div></div>
  <div class="product" style="left:613px;top:956px"><div class="thumb" role="img" aria-label="Octagonal wooden cigar ashtray" style="background:linear-gradient(160deg,#a3a3a3,#5e1a17)"></div><div class="name">CIGARASHTRAY</div><div class="price">$29.00 USD</div></div>
  <div class="product" style="left:860px;top:956px"><div class="thumb" role="img" aria-label="Heavy silver ring with gold cross" style="background:radial-gradient(circle,#d9c16a,#8d8d8d 55%,#2a2a2a)"></div><div class="name">HEAVYRING</div><div class="price">$29.00 USD</div></div>
</section>

<section class="mens-jewelry">
  <div class="photo" role="img" aria-label="Silver cufflinks on weathered wood" style="left:79px;top:1317px;width:337px;height:477px;background:linear-gradient(135deg,#8a7a62,#4a3d2c 60%,#2c241a)"></div>
  <div class="photo" role="img" aria-label="Pearl and chain necklace on black leather" style="left:416px;top:1317px;width:342px;height:477px;background:linear-gradient(135deg,#5a5a5a,#262626 55%,#0f0f0f)"></div>
  <h2 class="abs display" style="left:853px;top:1390px;font-size:52px">Men's<br>Jewelry</h2>
  <p class="abs lede" style="left:853px;top:1517px;width:220px">Lorem ipsum dolor sit amet, consectetur adipiscing elit, sed do eiusmod tempor inc didunt ut labore et dolore magna.</p>
  <a class="btn" style="left:853px;top:1649px">SHOP NOW</a>
</section>

<section class="cigar-bar">
  <h2 class="abs display" style="left:137px;top:2003px;font-size:52px">Cigar and Bar<br>Accessories</h2>
  <p class="abs lede" style="left:135px;top:2131px;width:345px">Lorem ipsum dolor sit amet, consectetur adipiscing elit, sed do eiusmod tempor inc didunt ut labore et dolore magnrem ipsum dolor sit amet, consectetur.</p>
  <a class="btn" style="left:135px;top:2258px">SHOP NOW</a>
  <div class="photo" role="img" aria-label="Wooden cigar cutter stand with chrome handle" style="left:565px;top:1973px;width:228px;height:333px;background:linear-gradient(180deg,#3a3a3a 0%,#6b2b1c 40%,#3c170e 100%);border-radius:6px"></div>
  <div class="photo" role="img" aria-label="Open wooden whiskey set case" style="left:821px;top:2026px;width:252px;height:272px;background:linear-gradient(160deg,#6a3a24,#2a1810);border-radius:4px"></div>
</section>

<section class="other-products">
  <div class="abs" style="left:79px;top:2508px;width:342px;height:433px;background:var(--panel)"></div>
  <h2 class="abs display" style="left:130px;top:2578px;font-size:52px">Other Men's<br>Products</h2>
  <p class="abs lede" style="left:128px;top:2708px;width:230px">Lorem ipsum dolor sit amet, consectetur adipiscing elit, sed do eiusmod tempor inc didunt ut labore et dolore magna.</p>
  <a class="btn" style="left:128px;top:2840px">SHOP NOW</a>
  <div class="photo" role="img" aria-label="Black and white close-up of chrome motorcycle exhaust" style="left:440px;top:2508px;width:337px;height:433px;background:linear-gradient(135deg,#d8d8d8,#5a5a5a 45%,#111 100%)"></div>
  <div class="photo" role="img" aria-label="Shaving brush and razor on a stand" style="left:777px;top:2508px;width:340px;height:433px;background:linear-gradient(160deg,#6d5a48,#b08860 45%,#d9d2c8 75%,#8d7a66)"></div>
</section>

<section class="about">
  <h2 class="abs display" style="left:126px;top:3080px;font-size:52px">About Ironvale Locker</h2>
  <div class="photo" role="img" aria-label="Man in a waistcoat smoking a cigar in a leather armchair" style="left:81px;top:3175px;width:566px;height:452px;background:radial-gradient(circle at 55% 45%,#4a3a30,#241a14 55%,#0e0a08)"></div>
  <div class="abs" style="left:675px;top:3175px;width:444px;height:452px;background:var(--panel)"></div>
  <p class="abs" style="left:725px;top:3260px;width:360px;font-size:14.5px;line-height:1.55;color:var(--muted)">Sed ut perspiciatis unde omnis iste natuserror sit voluptatem accusantium doloremque lud antium, totam rem aperiam, eaque ipsa quae ab illo inventore veritatis et quasi architecto beatae vitae dicta sunt explicabo. Nemo enim ipsam voluptatem quia voluptas sit asperatur aut odit aut fugit, sed quia consequuntur ma gni dolores eos qui ratione voluptatem squi nesciunt. Neque porro quisquam est, qui dolorem ipsum quia dolor sit amet.</p>
  <a class="btn" style="left:725px;top:3517px">READ MORE</a>
</section>

<section class="newsletter abs" style="left:0;top:3757px;width:1200px;height:321px;background:linear-gradient(100deg,#c9a23f 0%,#e9d9a6 45%,#f0e2b6 55%,#c9a23f 100%)">
  <h2 class="abs display" style="left:0;width:1200px;top:68px;text-align:center;font-size:46px;color:#111">Sign Up Newsletter</h2>
  <p class="abs" style="left:0;width:1200px;top:128px;text-align:center;font-size:15px;color:#222">Sed ut perspiciatis unde omnis iste natuserror sit volu</p>
  <div class="abs" style="left:354px;top:184px;width:491px;height:51px;border:2px solid #222;display:flex;align-items:center;padding:0 14px;justify-content:space-between">
    <span style="font-size:14px;color:#222">Email:</span>
    <svg width="20" height="16" viewBox="0 0 20 16"><path d="M2 8 H17 M11 2 L17 8 L11 14" fill="none" stroke="#111" stroke-width="2.4"/></svg>
  </div>
</section>

<footer class="site-footer">
  <h3 class="abs display" style="left:131px;top:4140px;font-size:30px">Links</h3>
  <a class="footer-link" style="top:4191px">Men's Jewelry</a>
  <a class="footer-link" style="top:4216px">Cigar &amp; Bar Products</a>
  <a class="footer-link" style="top:4240px">Man Cave Swag</a>
  <div class="abs" style="left:0;width:1200px;top:4205px;text-align:center;font-size:20px;font-weight:600;color:var(--gold)">Ironvale Locker</div>
  <h3 class="abs display" style="left:870px;width:200px;text-align:right;top:4140px;font-size:30px">About</h3>
  <p class="abs" style="left:790px;width:280px;top:4191px;text-align:right;font-size:14px;line-height:1.75;color:var(--muted)">Lorem ipsum dolor sit amet, cons ectetur adipiscing elit, sed do eius mod tempor incididunt ut la.</p>
  <div class="abs" style="left:539px;top:4330px;display:flex;gap:31px">
    <span role="img" aria-label="Social profile" style="width:20px;height:20px;border-radius:3px;background:#fff"></span>
    <span role="img" aria-label="Social profile" style="width:20px;height:20px;border-radius:50%;background:#fff"></span>
    <span role="img" aria-label="Video channel" style="width:20px;height:20px;border-radius:3px;background:#fff"></span>
  </div>
  <div class="abs" style="left:126px;top:4380px;width:946px;height:1px;background:#444"></div>
  <div class="abs" style="left:0;width:1200px;top:4415px;text-align:center" role="img" aria-label="Accepted payment methods">
    <span class="card-badge"></span><span class="card-badge"></span><span class="card-badge"></span><span class="card-badge"></span><span class="card-badge"></span><span class="card-badge"></span>
  </div>
  <p class="abs" style="left:0;width:1200px;top:4460px;text-align:center;font-size:14px;color:var(--muted)">© 2023 Ironvale Locker. All rights reserved.</p>
</footer>

</body>
</html>
```